New Australian Beverage Company Needs a Bottle Label Design

We are after a bottle label design for our new aloe vera drinks called 'Bold Finch'.

There are 5+ different colourrs we would like to compliment the flavors.

We are after a logo that is simple and eye catching.
Updates

Target Market(s)

Our target market is open for all as we would like to supply our drinks to quench everyone's thirst, however our biggest customers would be the teenagers to adults up to around the age of 50.

Industry/Entity Type

It Company

Requirements
Must have
• We are after a refreshing label that catches the eyes and makes you feel like picking it up and drinking it.

```html
<!DOCTYPE html>
<html lang="en">
<head>
<meta charset="utf-8">
<title>Bold Finch – Raspberry Flavour Label</title>
<link rel="stylesheet" href="https://fonts.googleapis.com/css2?family=Comfortaa:wght@600&family=Nunito:wght@800&family=Shadows+Into+Light&display=swap">
<style>
  :root {
    --backdrop: #eef2ec;
    --label-red: #d81b45;
    --label-red-deep: #c01339;
    --label-white: #ffffff;
    --ink-red: #d0243f;
    --visual-ice: #dfe4e8;
    --visual-leaf: #6f9a45;
  }
  html, body {
    margin: 0;
    padding: 0;
    width: 1200px;
    height: 1034px;
    overflow: hidden;
    background: var(--backdrop);
  }
  .canvas {
    position: relative;
    width: 1200px;
    height: 1034px;
  }
  .label {
    position: absolute;
    left: 365px;
    top: 47px;
    width: 470px;
    height: 940px;
    background: var(--label-white);
    overflow: hidden;
    box-shadow: 0 6px 24px rgba(0,0,0,0.12);
  }
  .label__header {
    position: absolute;
    left: 0; top: 0;
    width: 100%;
    height: 300px;
    background: var(--label-red);
  }
  .brand-name {
    position: absolute;
    left: 0; top: 40px;
    width: 100%;
    margin: 0;
    text-align: center;
    font-family: "Comfortaa", sans-serif;
    font-weight: 600;
    color: var(--label-white);
    font-size: 104px;
    line-height: 100px;
    letter-spacing: -2px;
  }
  .brand-name span { display: block; }
  .leaf-emblem {
    position: absolute;
    top: 196px;
    width: 44px;
    height: 44px;
  }
  .leaf-emblem--left { left: 30px; }
  .leaf-emblem--right { right: 30px; }
  .flavour {
    position: absolute;
    left: 0; top: 340px;
    width: 100%;
    margin: 0;
    text-align: center;
    font-family: "Shadows Into Light", cursive;
    color: var(--ink-red);
    font-size: 60px;
    line-height: 1;
    transform: rotate(-2deg);
  }
  .visual {
    position: absolute;
    left: 70px;
    top: 430px;
    width: 330px;
    height: 330px;
  }
  .label__footer {
    position: absolute;
    left: 0; top: 770px;
    width: 100%;
    height: 170px;
  }
  .volume {
    position: absolute;
    left: 0; top: 832px;
    width: 100%;
    text-align: center;
    font-family: "Nunito", sans-serif;
    font-weight: 800;
    color: var(--label-white);
    font-size: 40px;
    line-height: 1;
    letter-spacing: 1px;
  }
</style>
</head>
<body>
<main class="canvas">
  <section class="label">
    <div class="label__header"></div>
    <h1 class="brand-name"><span>bold</span><span>finch</span></h1>
    <svg class="leaf-emblem leaf-emblem--left" viewBox="0 0 44 44" aria-hidden="true">
      <circle cx="22" cy="22" r="18" fill="none" stroke="var(--label-white)" stroke-width="3"/>
    </svg>
    <svg class="leaf-emblem leaf-emblem--right" viewBox="0 0 44 44" aria-hidden="true">
      <circle cx="22" cy="22" r="18" fill="none" stroke="var(--label-white)" stroke-width="3"/>
    </svg>

    <p class="flavour">raspberry flavour</p>

    <svg class="visual" viewBox="0 0 330 330" role="img" aria-label="Illustration of ice cubes with a sprig of fresh leaves">
      <defs>
        <radialGradient id="visualTone" cx="50%" cy="50%" r="50%">
          <stop offset="0%" stop-color="var(--visual-leaf)" stop-opacity="0.5"/>
          <stop offset="55%" stop-color="var(--visual-ice)" stop-opacity="0.8"/>
          <stop offset="100%" stop-color="var(--label-white)" stop-opacity="0"/>
        </radialGradient>
      </defs>
      <rect width="330" height="330" fill="url(#visualTone)"/>
    </svg>

    <svg class="label__footer" viewBox="0 0 470 170" preserveAspectRatio="none">
      <path d="M0 30 C 120 0, 300 0, 470 22 L470 170 L0 170 Z" fill="var(--label-red)"/>
      <path d="M0 30 C 120 0, 300 0, 470 22 L470 36 C 300 14, 120 14, 0 44 Z" fill="var(--label-red-deep)" opacity="0.35"/>
    </svg>
    <div class="volume">500ml</div>
  </section>
</main>
</body>
</html>
```